Business Cards/Stationary for Statistical Consulting Firm
Cobalt Heron Analytics Group, LLC
Business Cards/Stationary for Statistical Consulting Firm - Consulting
Creative Brief
Use same font as used in my logo
Feel free to try new fonts.
Professional
Trevor Dunne-Morcott
Statistical Analyst
517 Upper Kestling Rd Weare, NH 03281
1-855-7GET-DATA
trevor@cobaltheronanalytics.example
www.cobaltheronanalytics.example
Single and Double Sided designs are both okay. Feel free to try different variations of the logo. Look at the website (www.cobaltheronanalytics.example) for ideas.

```html
<!DOCTYPE html>
<html lang="en">
<head>
<meta charset="utf-8">
<title>Cobalt Heron Analytics Group — Stationery</title>
<link href="https://fonts.googleapis.com/css2?family=Cinzel:wght@500&family=Open+Sans:wght@400;600&display=swap" rel="stylesheet">
<style>
  :root{
    --bg:#3b3b3b;
    --paper:#ffffff;
    --ink:#2b2b2b;
    --muted:#6d6d6d;
    --swoosh-dark:#2e2e2e;
    --swoosh-mid:#6a6a6a;
    --swoosh-light:#b9b9b9;
    --folder:#454545;
    --folder-dark:#2f2f2f;
  }
  *{box-sizing:border-box;margin:0;padding:0}
  html,body{width:1200px;height:379px;overflow:hidden;background:var(--bg)}
  body{position:relative;font-family:"Open Sans",Arial,sans-serif;color:var(--ink)}
  .item{position:absolute;background:var(--paper);overflow:hidden;box-shadow:0 3px 10px rgba(0,0,0,.45)}
  .swoosh{position:absolute;left:0;bottom:0;width:100%}
  .brand{display:flex;align-items:center;gap:5px}
  .brand-dot{width:12px;height:12px;border-radius:50%;background:var(--ink);flex:none}
  .brand-name{font-family:"Cinzel",Georgia,serif;font-weight:500;font-size:8px;letter-spacing:.3px;color:var(--ink);line-height:1.15}
  .small{font-size:5px;line-height:1.5;color:var(--muted)}
  /* business cards */
  .card{width:150px;height:88px}
  .card-front{left:20px;top:80px;background:var(--folder-dark)}
  .card-front .brand{position:absolute;left:12px;top:30px}
  .card-front .brand-dot{background:#e6e6e6}
  .card-front .brand-name{color:#e6e6e6}
  .card-back{left:20px;top:182px}
  .card-back .person{position:absolute;left:10px;top:10px}
  .person-name{font-size:7px;font-weight:600;color:var(--ink)}
  .person-role{font-size:5px;color:var(--muted);margin-bottom:4px}
  /* letterheads */
  .letter{width:190px;height:262px;top:58px}
  .letter-one{left:190px}
  .letter-two{left:396px}
  .letter .brand{position:absolute;left:16px;top:18px}
  .letter .address{position:absolute;left:16px;top:44px}
  .letter .body-lines{position:absolute;left:16px;right:20px;top:86px}
  .body-lines span{display:block;height:2px;background:#e6e6e6;margin-bottom:7px}
  /* envelopes */
  .envelope{width:236px;height:112px;left:604px}
  .env-front{top:58px}
  .env-front .brand{position:absolute;left:12px;top:12px}
  .env-front .address{position:absolute;left:12px;top:32px}
  .env-back{top:190px;background:#f4f4f4}
  .env-back .flap{position:absolute;left:0;top:0;width:100%;height:62px}
  .env-back .brand{position:absolute;left:50%;top:72px;transform:translateX(-50%)}
  /* folder */
  .folder{width:160px;height:262px;top:58px;background:var(--folder)}
  .folder-front{left:1020px}
  .folder-front .brand{position:absolute;left:50%;top:96px;transform:translateX(-50%);flex-direction:column;gap:8px;text-align:center}
  .folder-front .brand-dot{width:22px;height:22px;background:#e6e6e6}
  .folder-front .brand-name{color:#e6e6e6;font-size:10px}
  .folder-inside{left:856px;background:var(--folder-dark)}
  .folder-inside .pocket{position:absolute;left:0;bottom:0;width:100%;height:92px;background:var(--folder)}
  .folder-inside .slot{position:absolute;left:38px;top:130px;width:80px;height:44px;border:1px solid #5a5a5a}
</style>
</head>
<body>

<!-- shared swoosh shape -->
<svg width="0" height="0" style="position:absolute">
  <defs>
    <linearGradient id="swooshFill" x1="0" y1="0" x2="1" y2="0">
      <stop offset="0" stop-color="#555"/>
      <stop offset="1" stop-color="#222"/>
    </linearGradient>
  </defs>
</svg>

<section class="item card card-front" aria-label="Business card front">
  <div class="brand"><span class="brand-dot"></span><span class="brand-name">Cobalt Heron<br>Analytics Group, LLC</span></div>
</section>

<section class="item card card-back" aria-label="Business card back">
  <div class="person">
    <p class="person-name">Trevor Dunne-Morcott</p>
    <p class="person-role">Statistical Analyst</p>
    <p class="small">517 Upper Kestling Rd Weare, NH 03281<br>1-855-7GET-DATA · trmorcott<br>trevor@cobaltheronanalytics.example<br>www.cobaltheronanalytics.example</p>
  </div>
  <svg class="swoosh" viewBox="0 0 150 30" preserveAspectRatio="none" height="30">
    <path d="M0 30 L0 27 Q90 26 150 2 L150 30 Z" fill="url(#swooshFill)"/>
    <path d="M0 25 Q90 24 150 0" stroke="var(--swoosh-light)" stroke-width="1" fill="none"/>
  </svg>
</section>

<section class="item letter letter-one" aria-label="Letterhead">
  <div class="brand"><span class="brand-dot"></span><span class="brand-name">Cobalt Heron<br>Analytics Group, LLC</span></div>
  <p class="small address">517 Upper Kestling Rd Weare, NH 03281<br>1-855-7GET-DATA<br>www.cobaltheronanalytics.example</p>
  <div class="body-lines"><span></span><span></span><span></span><span></span><span></span><span></span><span></span><span style="width:60%"></span></div>
  <svg class="swoosh" viewBox="0 0 190 70" preserveAspectRatio="none" height="70">
    <path d="M0 70 L0 64 Q120 60 190 4 L190 70 Z" fill="url(#swooshFill)"/>
    <path d="M0 60 Q120 56 190 0" stroke="var(--swoosh-light)" stroke-width="1.2" fill="none"/>
  </svg>
</section>

<section class="item letter letter-two" aria-label="Letterhead, second page">
  <div class="brand"><span class="brand-dot"></span><span class="brand-name">Cobalt Heron<br>Analytics Group, LLC</span></div>
  <p class="small address">trevor@cobaltheronanalytics.example<br>1-855-7GET-DATA</p>
  <div class="body-lines"><span></span><span></span><span></span><span></span><span style="width:70%"></span></div>
  <svg class="swoosh" viewBox="0 0 190 70" preserveAspectRatio="none" height="70">
    <path d="M0 70 L0 64 Q120 60 190 4 L190 70 Z" fill="url(#swooshFill)"/>
    <path d="M0 60 Q120 56 190 0" stroke="var(--swoosh-light)" stroke-width="1.2" fill="none"/>
  </svg>
</section>

<section class="item envelope env-front" aria-label="Envelope front">
  <div class="brand"><span class="brand-dot"></span><span class="brand-name">Cobalt Heron Analytics Group, LLC</span></div>
  <p class="small address">517 Upper Kestling Rd Weare, NH 03281</p>
  <svg class="swoosh" viewBox="0 0 236 36" preserveAspectRatio="none" height="36">
    <path d="M0 36 L0 33 Q150 30 236 2 L236 36 Z" fill="url(#swooshFill)"/>
    <path d="M0 30 Q150 27 236 0" stroke="var(--swoosh-light)" stroke-width="1" fill="none"/>
  </svg>
</section>

<section class="item envelope env-back" aria-label="Envelope back">
  <svg class="flap" viewBox="0 0 236 62" preserveAspectRatio="none">
    <path d="M0 0 L118 58 L236 0 Z" fill="#e2e2e2" stroke="#cfcfcf"/>
  </svg>
  <div class="brand"><span class="brand-dot"></span><span class="brand-name">Cobalt Heron Analytics Group, LLC</span></div>
</section>

<section class="item folder folder-inside" aria-label="Presentation folder, inside">
  <div class="pocket"></div>
  <div class="slot"></div>
</section>

<section class="item folder folder-front" aria-label="Presentation folder, cover">
  <div class="brand"><span class="brand-dot"></span><span class="brand-name">Cobalt Heron<br>Analytics Group, LLC</span></div>
</section>

</body>
</html>
```